BRANTWELL & BRANTWELL,LLP NEEDS A NEW LETTERHEAD DESIGN

a conservative yet contemporary layout befitting a long established
firm, consistent with the times, some form of logo so it catches ones attention, and is
admirable, but portrays integrity
Updates

I would like to approve #22066987 Please advise how to do this as it’s confusing on the site so I can approve payment for the designer

Target Market(s)

real estate investors and building management people

Industry/Entity Type

Law Firm

Font styles to use
Serif

Colors

Designer to choose colors to be used in the design.

Requirements
Must have
• some form of conservative logo

```html
<!DOCTYPE html>
<html lang="en">
<head>
<meta charset="utf-8">
<title>Brantwell &amp; Brantwell LLP Letterhead</title>
<link href="https://fonts.googleapis.com/css2?family=Lato:wght@400&family=Arimo&display=swap" rel="stylesheet">
<style>
  :root {
    --backdrop: #cdcdcd;
    --paper: #f6f6f7;
    --navy: #1d3a5f;
    --body-ink: #5a5a5e;
    --footer-ink: #3a3a3e;
  }
  html, body {
    margin: 0;
    padding: 0;
    width: 1200px;
    height: 994px;
    overflow: hidden;
    background: var(--backdrop);
  }
  .letterhead {
    position: absolute;
    left: 257px;
    top: 17px;
    width: 688px;
    height: 960px;
    background: var(--paper);
    box-shadow: 0 6px 24px rgba(0,0,0,0.18);
  }
  .masthead {
    position: absolute;
    top: 24px;
    left: 0;
    width: 100%;
    text-align: center;
  }
  .masthead-mark {
    display: block;
    width: 26px;
    height: 26px;
    margin: 0 auto 38px;
    background: var(--navy);
  }
  .firm-name {
    font-family: "Lato", sans-serif;
    font-weight: 400;
    font-size: 14px;
    letter-spacing: 0.6px;
    color: var(--navy);
    margin: 0;
    line-height: 18px;
  }
  .letter {
    position: absolute;
    left: 111px;
    top: 243px;
    width: 507px;
    font-family: "Lato", sans-serif;
    font-size: 11.2px;
    line-height: 18.3px;
    color: var(--body-ink);
  }
  .letter p {
    margin: 0 0 18.3px;
    text-align: justify;
  }
  .letter .salutation { text-align: left; }
  .letter .closing { margin-top: 54px; text-align: left; }
  .footer-bar {
    position: absolute;
    left: 0;
    top: 897px;
    width: 9px;
    height: 37px;
    background: var(--navy);
  }
  .footer-contact {
    position: absolute;
    left: 52px;
    top: 899px;
    font-family: "Arimo", sans-serif;
    font-size: 11px;
    line-height: 13.6px;
    color: var(--footer-ink);
  }
  .footer-contact .footer-firm { color: var(--navy); }
  .footer-contact .contact-line {
    display: flex;
    align-items: center;
    gap: 4px;
  }
  .footer-contact svg { width: 8px; height: 8px; }
  .footer-contact .spacer { width: 5px; }
  .footer-web {
    position: absolute;
    right: 55px;
    top: 926px;
    font-family: "Arimo", sans-serif;
    font-size: 11px;
    color: var(--footer-ink);
  }
</style>
</head>
<body>
  <div class="letterhead">
    <header class="masthead">
      <span class="masthead-mark"></span>
      <h1 class="firm-name">Brantwell &amp; Brantwell, LLP</h1>
    </header>

    <main class="letter">
      <p class="salutation">Dear Daniel Whitcombe,</p>
      <p>Lorem ipsum dolor sit amet, consectetuer adipiscing elit, sed diam nonummy nibh euismod tincidunt ut laoreet dolore magna aliquam erat volutpat. Ut wisi enim ad minim veniam, quis nostrud exerci tation ullamcorper suscipit lobortis nisl ut aliquip ex ea commodo consequat. Duis dolore te feugait nulla facilisi. Nam liber tempor cum soluta nobis eleifend option congue nihil imperdiet doming id quod mazim placerat facer possim assum. Lorem ipsum dolor sit amet, consectetuer adipiscing elit, sed diam nonummy nibh euismod tincidunt ut laoreet dolore magna aliquam erat volutpat. Ut wisi enim ad minim veniam, quis nostrud exerci tation ullamcorper suscipit lobortis nisl ut aliquip ex ea commodo consequat.</p>
      <p>Consectetuer adipiscing elit, sed diam nonummy nibh euismod tincidunt ut laoreet dolore magna aliquam erat volutpat. Ut wisi enim ad minim veniam, quis nostrud exerci tation ullamcorper suscipit lobortis nisl ut aliquip ex ea commodo consequat. Consectetuer adipiscing elit, sed diam nonummy nibh euismod tincidunt ut laoreet dolore magna aliquam erat volutpat. Ut wisi enim ad minim veniam, quis nostrud exerci tation ullamcorper suscipit lobortis nisl ut aliquip ex ea commodo consequat.</p>
      <p>Consectetuer adipiscing elit, sed diam nonummy nibh euismod tincidunt ut laoreet dolore magna aliquam erat volutpat. Ut wisi enim ad minim veniam, quis nostrud exerci tation ullamcorper suscipit lobortis nisl ut aliquip ex ea commodo consequat. Consectetuer adipiscing elit, sed diam nonummy nibh euismod tincidunt ut laoreet dolore magna aliquam erat volutpat. Ut wisi enim ad minim veniam, quis nostrud exerci tation ullamcorper suscipit lobortis nisl ut aliquip ex ea commodo consequat.</p>
      <p class="closing">Sincerely Yours</p>
    </main>

    <footer>
      <div class="footer-bar"></div>
      <div class="footer-contact">
        <div class="footer-firm">Brantwell &amp; Brantwell, LLC</div>
        <div>48 Harbor Street Suite 210, Easton, New York 10990</div>
        <div class="contact-line">
          <svg viewBox="0 0 10 10" aria-hidden="true"><path d="M2 1 L4 1 L4.6 3.2 L3.4 4 Q4.3 5.8 6 6.6 L6.8 5.4 L9 6 L9 8 Q8.5 9 7.5 9 Q1 8 1 2.5 Q1 1.5 2 1 Z" fill="var(--navy)"/></svg>
          <span>(555) 014-2271</span>
          <span class="spacer"></span>
          <svg viewBox="0 0 10 10" aria-hidden="true"><rect x="2.5" y="0.5" width="5" height="3" fill="var(--navy)"/><rect x="0.5" y="3.5" width="9" height="4" rx="1" fill="var(--navy)"/><rect x="2.5" y="6.5" width="5" height="3" fill="var(--navy)"/></svg>
          <span>(555)-014-2290</span>
          <span class="spacer"></span>
          <svg viewBox="0 0 10 10" aria-hidden="true"><rect x="0.7" y="2" width="8.6" height="6" fill="none" stroke="var(--navy)" stroke-width="1"/><path d="M0.7 2 L5 5.5 L9.3 2" fill="none" stroke="var(--navy)" stroke-width="1"/></svg>
          <span>info@bbrelaw.com</span>
        </div>
      </div>
      <div class="footer-web">www.BrantwellLaw.com</div>
    </footer>
  </div>
</body>
</html>
```